Bright Harbor Counseling Letterhead for hip modern business

I would like some ombre use of the colors in the logo hip letterhead that incorporates logo colors and feel, needs to connect with young professionals and college students. i need to be able to write letters to schools to excuse absences as well. i like color blocks on one side preferably using colors from the attached logo design.

Target Market(s)

high income young people, young adults and college students

Industry/Entity Type

mental health

Font styles to use
Serif
Sans Serif

Colors
0054AA
0677BA
7BADD7
CADEEF
E8F1F8
0094D4
00A9DD
6FCCEA
C7EBF8
E9F6FB
00AB8E
00BBA5
67D7C9
C6EFE9
E9F9F6
59FF00
82FF00
B8FF75
E3FFCB
F4FFEA
A7469A
B969AE
D3A5CF
EDDBEB
F8F0F9
6B429C
8869AF
B7A5CE
E3DAEB
F3F0F8

Requirements
Must have
• a modern hip feel, somewhat color

```html
<!DOCTYPE html>
<html lang="en">
<head>
<meta charset="utf-8">
<title>Bright Harbor Counseling Letterhead</title>
<link href="https://fonts.googleapis.com/css2?family=Open+Sans:wght@300;400;700&display=swap" rel="stylesheet">
<style>
  :root {
    --backdrop: #bcd7f0;
    --paper: #ffffff;
    --ink: #3b3b3b;
    --ink-soft: #6a6a6a;
    --purple: #8e3a96;
    --teal: #5bbfb5;
    --blue: #3a6db5;
    --contact-blue: #2e86c8;
    --tile: #ece4f1;
    --tile-blue: #e6edf6;
  }
  * { box-sizing: border-box; margin: 0; padding: 0; }
  html, body {
    width: 1200px; height: 784px; overflow: hidden;
    background: var(--backdrop);
    font-family: "Open Sans", Arial, sans-serif;
  }
  .letterhead {
    position: absolute; left: 320px; top: 30px;
    width: 560px; height: 724px;
    background: var(--paper);
    box-shadow: 0 6px 18px rgba(40, 80, 130, 0.18);
    overflow: hidden;
  }
  .brand {
    position: absolute; left: 34px; top: 30px;
    color: var(--ink);
  }
  .brand-name {
    font-weight: 300; font-size: 27px; line-height: 1.05; letter-spacing: 0.5px;
  }
  .brand-sub {
    font-weight: 300; font-size: 11px; letter-spacing: 3.4px;
    text-align: right; margin-top: 2px;
  }
  .brand-dot {
    position: absolute; left: 268px; top: 36px;
    width: 22px; height: 22px; border-radius: 50%;
    background: var(--purple);
  }
  .corner-tiles { position: absolute; right: 0; top: 0; }
  .contact {
    position: absolute; right: 44px; top: 78px;
    text-align: right; font-size: 7.5px; line-height: 1.7;
  }
  .contact-address { color: var(--contact-blue); font-weight: 700; }
  .contact-lines { color: var(--ink-soft); }
  .contact-icon {
    display: inline-block; width: 7px; height: 7px; border-radius: 50%;
    border: 1px solid var(--contact-blue); vertical-align: -1px; margin: 0 3px 0 5px;
  }
  .rule { position: absolute; left: 250px; right: 0; height: 3px; }
  .rule-purple { top: 106px; background: var(--purple); }
  .rule-blue { top: 112px; background: var(--blue); }
  .color-band {
    position: absolute; left: 0; right: 0; bottom: 0; height: 9px;
    display: flex; gap: 3px;
  }
  .band-purple { flex: 0 0 27%; background: var(--purple); }
  .band-teal { flex: 0 0 36%; background: var(--teal); }
  .band-blue { flex: 1; background: var(--blue); }
</style>
</head>
<body>
  <main class="letterhead">
    <svg class="corner-tiles" width="120" height="110" viewBox="0 0 120 110" aria-hidden="true">
      <rect x="62" y="6" width="26" height="18" fill="var(--tile)"/>
      <rect x="90" y="0" width="30" height="30" fill="var(--tile-blue)"/>
      <rect x="70" y="34" width="34" height="28" fill="var(--tile-blue)"/>
      <rect x="106" y="40" width="14" height="36" fill="var(--tile)"/>
    </svg>

    <header class="brand">
      <div class="brand-name">Bright Harbor</div>
      <div class="brand-sub">Counseling</div>
    </header>
    <span class="brand-dot" aria-hidden="true"></span>

    <address class="contact">
      <div class="contact-address"><span class="contact-icon"></span>4120 Tidewater Ave, Ste 210, California, 93101, United States</div>
      <div class="contact-lines">
        <span class="contact-icon"></span>(000) 000-0000
        <span class="contact-icon"></span>(000) 000-0000
        <span class="contact-icon"></span>hello@brightharborcare.com
        <span class="contact-icon"></span>www.brightharborcare.com
      </div>
    </address>

    <div class="rule rule-purple"></div>
    <div class="rule rule-blue"></div>

    <footer class="color-band" aria-hidden="true">
      <span class="band-purple"></span>
      <span class="band-teal"></span>
      <span class="band-blue"></span>
    </footer>
  </main>
</body>
</html>
```